Rock, Paper Scissors Championship Flyer

We need a dynamic, bold and exciting flyer to promote the following event at our sports center. The event will be primarily focused for adults, but children are welcome to join

Rock, Paper, Scissors Championship - $$$ prizes
Date: June 9th, 2018
Time: 11am-4pm
Fee: $2 to enter, free for spectators
Heats to determine the overall ‘Rock, Paper, Scissors’ champion!
- Cash prizes on offer
- Live music.
- Food and beverage available for purchase

Belvorrow Sports Center, Roselle NJ
908-555-3162
www.belvorrowgrounds.example

Must include our logo (does not have to be huge) and County seal (both attached)

Colors

Designer to choose colors to be used in the design.

Requirements
Must have
• Should be fun and colorful
• The following info and attached logos:
• Rock, Paper, Scissors Championship - $$$ prizes
• Date: June 9th, 2018
• Time: 11am-4pm
• Fee: $2 to enter, free for spectators
• Heats to determine the overall ‘Rock, Paper, Scissors’ champion!
• - Cash prizes on offer
• - Live music.
• - Food and beverage available for purchase
• Belvorrow Sports Center, Roselle NJ
• 908-555-3162
• www.belvorrowgrounds.example
Nice to have
• There are a few inspirational photos attached to give an idea of what we are looking for.

```html
<!DOCTYPE html>
<html lang="en">
<head>
<meta charset="utf-8">
<title>Rock Paper Scissors Championship</title>
<link rel="stylesheet" href="https://fonts.googleapis.com/css2?family=Bowlby+One&family=Poppins:ital,wght@0,400;0,500;0,600;0,700;0,800;1,800;1,900&display=swap">
<style>
  :root {
    --sun-yellow: #ffd21f;
    --sun-orange: #f7a81b;
    --sky-blue: #1f63be;
    --deep-blue: #164a97;
    --navy: #1b2c58;
    --ink: #151a26;
    --paper: #ffffff;
    --gold: #ffd23a;
    --tag-yellow: #f9c21a;
  }
  * { box-sizing: border-box; margin: 0; padding: 0; }
  html, body { width: 848px; height: 1200px; overflow: hidden; background: #e9eaee; }
  .flyer {
    position: relative; width: 848px; height: 1200px; overflow: hidden;
    background: radial-gradient(circle at 60% 22%, #fff6b8 0%, var(--sun-yellow) 28%, var(--sun-orange) 70%);
    font-family: "Poppins", sans-serif; color: var(--paper);
  }
  .backdrop { position: absolute; inset: 0; }
  .brand {
    position: absolute; left: 40px; top: 56px; width: 130px;
    display: flex; flex-direction: column; align-items: center; gap: 8px;
    color: var(--navy); font-weight: 700; font-size: 13px; line-height: 1.2; text-align: center;
  }
  .brand-dot { width: 44px; height: 44px; border-radius: 50%; background: var(--navy); }
  .seal { position: absolute; left: 699px; top: 39px; width: 104px; height: 104px; border-radius: 50%; background: #efe7cf; border: 4px solid #c99a3a; }
  .hand { position: absolute; background: var(--sky-blue); border-radius: 30px; }
  .hand-rock { left: 185px; top: 168px; width: 120px; height: 110px; transform: rotate(-8deg); }
  .hand-paper { left: 330px; top: 200px; width: 170px; height: 110px; transform: rotate(8deg); }
  .hand-scissors { left: 515px; top: 160px; width: 200px; height: 105px; transform: rotate(10deg); }
  .title-banner {
    position: absolute; left: 50px; top: 335px; width: 748px; height: 140px;
    background: var(--ink); clip-path: polygon(0 8%, 100% 0, 98% 100%, 2% 94%);
    border: 0;
  }
  .title {
    position: absolute; left: 50px; top: 350px; width: 748px; text-align: center;
    font-family: "Bowlby One", sans-serif; font-size: 70px; line-height: 58px; letter-spacing: 2px;
    color: var(--paper); text-shadow: 0 4px 0 #9aa3b2;
  }
  .title .star { color: var(--gold); font-size: 44px; vertical-align: 12px; }
  .subtitle {
    position: absolute; left: 256px; top: 506px; width: 330px; height: 44px;
    background: var(--paper); border: 3px solid var(--sky-blue);
    transform: skewX(-10deg);
    display: flex; align-items: center; justify-content: center;
  }
  .subtitle span { transform: skewX(10deg); font-weight: 900; font-style: italic; font-size: 27px; color: var(--sky-blue); letter-spacing: 1px; }
  .fee {
    position: absolute; left: 0; top: 660px; width: 848px; text-align: center;
    font-weight: 800; font-size: 30px; color: var(--deep-blue); font-variant: small-caps; letter-spacing: 0.5px;
  }
  .trophy { position: absolute; left: 14px; top: 734px; width: 214px; height: 262px; background: linear-gradient(180deg, #ffc93a, #f29a2e 70%, #e08a5e); border-radius: 50% 50% 20px 20px / 35% 35% 20px 20px; }
  .when {
    position: absolute; left: 316px; top: 809px; width: 532px; height: 58px;
    border-top: 2px solid rgba(255,255,255,.55); border-bottom: 2px solid rgba(255,255,255,.55); border-left: 2px solid rgba(255,255,255,.55);
    display: flex; align-items: center; padding-left: 16px;
    color: var(--gold); font-weight: 600; font-size: 31px; white-space: pre;
  }
  .venue { position: absolute; left: 442px; top: 872px; font-weight: 700; font-size: 25px; line-height: 42px; }
  .venue .town { padding-left: 150px; }
  .features { position: absolute; left: 372px; top: 982px; list-style: none; }
  .features li { display: flex; align-items: center; height: 42px; font-size: 17px; }
  .features svg { width: 34px; height: 34px; margin-right: 24px; }
  .heats-tag {
    position: absolute; left: 0; top: 1004px; width: 242px; height: 36px;
    background: var(--tag-yellow); clip-path: polygon(0 0, 100% 0, 94% 100%, 0 100%);
    display: flex; align-items: center; padding-left: 20px;
    font-weight: 700; font-size: 17px; letter-spacing: .5px;
  }
  .champion-box {
    position: absolute; left: 0; top: 1040px; width: 314px; height: 100px; background: var(--paper);
    display: flex; flex-direction: column; align-items: center; justify-content: center;
    color: var(--deep-blue); font-weight: 800; font-size: 22px; line-height: 32px;
  }
  .champion-box .quoted { font-variant: small-caps; }
  .champion-box .champ { font-size: 25px; letter-spacing: 1px; }
  .footer {
    position: absolute; left: 0; top: 1140px; width: 848px; height: 60px; background: var(--navy);
    display: flex; align-items: center; gap: 46px; padding-left: 83px;
    font-size: 18px; letter-spacing: 1px; color: #dfe6f4;
  }
  .footer b { color: var(--paper); font-weight: 600; }
</style>
</head>
<body>
<main class="flyer">
  <svg class="backdrop" width="848" height="1200" viewBox="0 0 848 1200" aria-hidden="true">
    <defs>
      <linearGradient id="sea" x1="0" y1="0" x2="0" y2="1">
        <stop offset="0" stop-color="#2a72cf"/>
        <stop offset="1" stop-color="#174a98"/>
      </linearGradient>
    </defs>
    <circle cx="425" cy="390" r="288" fill="#ffffff"/>
    <path d="M0 520 Q 424 640 848 520 L848 1200 L0 1200 Z" fill="url(#sea)"/>
    <path d="M0 540 Q 424 660 848 540 L848 580 Q 424 690 0 580 Z" fill="#ffffff" opacity=".9"/>
    <path d="M0 648 L848 640 L848 716 L0 722 Z" fill="#ffffff"/>
    <circle cx="425" cy="330" r="70" fill="#1f63be"/>
  </svg>

  <div class="brand"><span class="brand-dot"></span>Belvorrow Sports Center</div>
  <div class="seal" aria-hidden="true"></div>

  <div class="hand hand-rock" role="img" aria-label="Illustration of a hand making a rock fist"></div>
  <div class="hand hand-paper" role="img" aria-label="Illustration of a flat open hand for paper"></div>
  <div class="hand hand-scissors" role="img" aria-label="Illustration of a hand making scissors with two fingers"></div>

  <div class="title-banner"></div>
  <h1 class="title">ROCK<span class="star">★</span>PAPER<br>SCISSORS</h1>
  <div class="subtitle"><span>CHAMPIONSHIP</span></div>

  <p class="fee">$2 to enter, free for spectators</p>

  <div class="trophy" role="img" aria-label="Illustration of a raised hand holding a gold trophy"></div>

  <p class="when">11am-4pm  June 9th, 2018</p>
  <p class="venue">Belvorrow Sports Center<br><span class="town">Roselle NJ</span></p>

  <ul class="features">
    <li><svg viewBox="0 0 34 34" fill="none" stroke="#fff" stroke-width="2"><rect x="4" y="10" width="26" height="16" rx="2"/><circle cx="17" cy="18" r="4"/></svg>Cash prizes on offer.</li>
    <li><svg viewBox="0 0 34 34" fill="none" stroke="#fff" stroke-width="2"><path d="M12 26V8l16-4v18"/><circle cx="9" cy="26" r="3.5"/><circle cx="25" cy="22" r="3.5"/></svg>Live music.</li>
    <li><svg viewBox="0 0 34 34" fill="none" stroke="#fff" stroke-width="2"><path d="M5 18h24a12 10 0 0 1-24 0z"/><path d="M14 6v8M20 4v10"/></svg>Food and beverage available for purchase.</li>
  </ul>

  <div class="heats-tag">HEATS TO DETERMINE</div>
  <div class="champion-box">
    <span class="quoted">‘Rock, Paper, Scissors’</span>
    <span class="champ">CHAMPION!!</span>
  </div>

  <footer class="footer">
    <span>Contact: <b>908-555-3162</b></span>
    <span>Homepage: <b>www.belvorrowgrounds.example</b></span>
  </footer>
</main>
</body>
</html>
```